Webdesign für Finanzberatung
Sehr schönes Design. Auf Änderungswünsche wurde sehr schnell reagiert. Bin sehr zufrieden!
Zielgruppe
Ganzheitliche Finanzberatung / Finanzcoaching (Geldanlage, Investment, ETFs, Fonds, Aktien) für eine digital affine Zielgruppe. Es handelt sich um eine Beratung / um ein Coaching gegen Honorar.
Aufgabenstellung
Die Webseite sollte die Elemente 'digital' (Roboter) und 'persönlich' (Mensch) kombinieren. Das Design sollte modern sein und eine digital affine Zielgruppe ansprechen. Gleichzeitig soll das Thema 'persönliche Finanzberatung' zum Ausdruck gebracht werden.

```html
<!DOCTYPE html>
<html lang="de">
<head>
<meta charset="utf-8">
<title>Kapitalruhe – Finanzen digitalisieren</title>
<link href="https://fonts.googleapis.com/css2?family=Roboto:wght@400;500;700&family=Roboto+Condensed:wght@700&display=swap" rel="stylesheet">
<style>
:root{
  --blue:#3f6b9c;
  --blue-dark:#1f3d63;
  --navy:#16294a;
  --ink:#222831;
  --text:#4a4f57;
  --light:#f3f4f6;
  --grey:#eeeeee;
  --line:#c9ced6;
  --white:#ffffff;
}
*{margin:0;padding:0;box-sizing:border-box}
html,body{width:1200px;height:3999px;overflow:hidden;background:var(--white)}
body{font-family:"Roboto",sans-serif;color:var(--ink)}
.page{position:relative;width:1200px;height:3999px;overflow:hidden}
.abs{position:absolute}
.btn{position:absolute;display:inline-flex;align-items:center;justify-content:center;gap:8px;border-radius:16px;font-size:11px;color:var(--white);background:var(--blue);height:28px;padding:0 16px}
.btn.ghost{background:transparent;border:1.5px solid var(--white)}
.btn-dark{background:var(--blue-dark)}
/* hero */
.hero{position:absolute;left:0;top:0;width:1200px;height:442px;overflow:hidden}
.hero-photo{position:absolute;inset:0;background:linear-gradient(110deg,#5d7ea7 0%,#2c4f7e 35%,#16335d 60%,#0f2547 80%,#1b3c6a 100%)}
.logo{position:absolute;display:flex;align-items:center;gap:8px}
.logo .dot{width:20px;height:20px;border-radius:50%;border:2px solid currentColor}
.logo span{font-weight:500;letter-spacing:2px;font-size:18px}
.nav{position:absolute;top:57px;left:492px;display:flex;gap:24px;font-size:11px;color:var(--white);align-items:center}
.nav .cta{background:var(--blue);padding:9px 8px;margin-left:28px}
.hero-title{position:absolute;top:165px;left:0;width:1200px;text-align:center;font-family:"Roboto Condensed",sans-serif;font-size:60px;color:var(--white);letter-spacing:1px}
/* section head */
.sec-head{position:absolute;left:0;width:1200px;text-align:center}
.sec-head .mark{width:50px;height:28px;margin:0 auto 12px;border:2px solid #c5cfdc;border-radius:14px}
.sec-head .kicker{color:var(--blue);font-size:21px}
.sec-head h2{font-size:26px;font-weight:700;color:var(--ink);margin-top:4px}
/* solution */
.sol-box{position:absolute;background:var(--white);box-shadow:0 2px 14px rgba(0,0,0,.1);padding:50px 40px}
.sol-box h3{font-size:17px;font-weight:400;line-height:1.3}
.sol-box h3 b{font-weight:500}
.sol-box p{font-size:9px;line-height:1.5;color:var(--text);margin-top:14px}
.ticks{list-style:none;margin-top:16px;font-size:8.5px;color:var(--text)}
.ticks li{margin-bottom:8px}
.ticks li::before{content:"✓";color:var(--blue);margin-right:10px}
/* pricing */
.price{position:absolute;top:1563px;width:255px;height:358px;background:linear-gradient(135deg,#e8ebef,#f6f7f9);padding:28px 14px;border:1px solid #e3e6ea}
.price h4{color:var(--blue);font-size:13px;font-weight:500;line-height:1.35}
.price .amt{font-size:15px;margin-top:4px;color:var(--ink)}
.price p{font-size:9px;font-weight:500;line-height:1.45;color:var(--text);margin-top:18px}
.price .ticks{margin-top:18px}
.price.featured{background:var(--blue);border-color:var(--blue)}
.price.featured h4,.price.featured .amt,.price.featured p,.price.featured .ticks,.price.featured .ticks li::before{color:var(--white)}
/* about */
.about{position:absolute;left:0;top:2032px;width:1200px;height:568px;background:var(--blue)}
.about-photo{position:absolute;left:0;top:0;width:551px;height:568px;overflow:hidden}
.about-text{position:absolute;left:629px;top:57px;width:340px;color:var(--white)}
.about-text .kicker{font-size:11px}
.about-text h2{font-size:25px;line-height:1.4;margin-top:4px}
.about-text p{font-size:9.5px;line-height:1.5;margin-top:12px;color:#e4ebf5}
.feature{display:flex;gap:12px;margin-top:24px}
.feature .ic{width:36px;height:36px;flex:none}
.feature h5{font-size:12px;font-weight:400;color:#cfe0f5}
.feature div p{font-size:8.5px;margin-top:4px}
/* news */
.news{position:absolute;top:2826px;width:224px;height:356px;background:#efefef;border-radius:8px;overflow:hidden}
.news .img{height:142px;position:relative}
.news .date{position:absolute;right:16px;bottom:0;background:var(--blue-dark);color:var(--white);font-size:9px;text-align:center;padding:4px 6px;width:40px;line-height:1.2}
.news .body{padding:12px 18px}
.news .cat{font-size:8px;color:var(--blue)}
.news h4{font-size:13px;font-weight:500;margin-top:14px;line-height:1.25}
.news p{font-size:8.5px;color:var(--text);line-height:1.5;margin-top:12px}
.news .arrow{position:absolute;left:18px;bottom:28px;width:40px;height:26px;border-radius:13px;background:var(--blue);color:var(--white);font-size:12px;display:flex;align-items:center;justify-content:center}
/* contact */
.contact-bg{position:absolute;left:0;top:3267px;width:1200px;height:460px;background:var(--light)}
.c-box{position:absolute;left:259px;top:3281px;width:221px;height:297px;background:var(--blue);color:var(--white);padding:26px 16px}
.c-shadow{position:absolute;left:271px;top:3293px;width:221px;height:297px;background:#5f86b5}
.c-item{display:flex;gap:14px;padding:18px 0;border-bottom:1px solid rgba(255,255,255,.35)}
.c-item:last-child{border:0}
.c-item h5{font-size:16px;font-weight:500}
.c-item p{font-size:9px;margin-top:3px}
.form{position:absolute;left:537px;top:3296px;width:413px}
.form .kicker{font-size:11px;color:var(--blue)}
.form h3{font-size:15px;font-weight:500;margin-top:6px}
.field{position:absolute;border-bottom:1px solid #b9bec6;font-size:9px;color:var(--blue);height:22px}
/* footer */
.foot-links{position:absolute;top:3812px;left:0;width:1200px;display:flex;justify-content:center;gap:22px;color:var(--white);font-size:11px;font-weight:500}
.copy{position:absolute;top:3841px;width:1200px;text-align:center;color:var(--white);font-size:10px}
</style>
</head>
<body>
<div class="page">

  <!-- hero -->
  <section class="hero">
    <div class="hero-photo" role="img" aria-label="Geschäftsmann mit Tablet und leuchtenden Finanzdiagrammen vor blauem Börsenhintergrund"></div>
    <svg class="abs" style="left:0;top:330px" width="1200" height="112" viewBox="0 0 1200 112"><path d="M0 95 C250 60 420 50 600 80 C820 115 1000 75 1200 38 L1200 112 L0 112Z" fill="#ffffff"/></svg>
    <div class="logo" style="left:174px;top:56px;color:var(--white)"><i class="dot"></i><span>KAPITALRUHE</span></div>
    <nav class="nav"><span>STARTSEITE</span><span>MEIN ANGEBOT</span><span>ÜBER MICH</span><span style="margin-left:14px">BLOG</span><span>KONTAKT</span><span class="cta">ERSTGESPRÄCH</span></nav>
    <h1 class="hero-title">FINANZENDIGITALISIEREN</h1>
    <span class="btn btn-dark" style="left:510px;top:244px;width:180px;font-size:11px">ERSTGESPRÄCH BUCHEN</span>
  </section>

  <!-- solution -->
  <div class="sec-head" style="top:497px"><div class="mark"></div><div class="kicker">LÖSUNG</div><h2>VERBINDUNG VON</h2></div>

  <div class="abs" style="left:174px;top:646px;width:426px;height:336px;background:linear-gradient(135deg,#3a3f47,#8d97a3 55%,#c9ccd1)" role="img" aria-label="Laptop mit schwebenden digitalen Finanzsymbolen"></div>
  <div class="sol-box" style="left:600px;top:646px;width:425px;height:336px">
    <h3>Automatisierung von<br><b>Finanzen mittels digitalen</b></h3>
    <p>Lorem ipsum dolor sit amet, consectetur adipisicing elit, sed do eiusmod tempor incididunt ut labore et dolore magna aliqua. Ut enim ad minim veniam quis nostrud exercitation ullamco laboris nisi ut aliquip ex ea commodo consequat. Duis aute irure dolor in reprehenderit in voluptate velit esse cillum dolore eu fugiat nulla pariatur. Excepteur sint occaecat cupidatat non proident, sunt culpa qui officia deserunt mollit anim id est laborum.</p>
    <p>Lorem ipsum dolor sit amet, consectetur adipisicing elit, sed do eiusmod tempor incididunt ut labore et dolore magna aliqua. Ut enim ad minim veniam quis nostrud exercitation ullamco laboris nisi ut aliquip ex ea commodo consequat.</p>
    <span class="btn" style="left:40px;top:246px">Weiterlesen →</span>
  </div>
  <div class="sol-box" style="left:174px;top:982px;width:426px;height:337px">
    <h3>persönliche Beratung bei<br><b>Finanzentscheidungen</b></h3>
    <p>Lorem ipsum dolor sit amet, consectetur adipisicing elit, sed do eiusmod tempor incididunt ut labore et dolore magna aliqua. Ut enim ad minim veniam quis nostrud exercitation ullamco laboris nisi ut aliquip ex ea commodo consequat.</p>
    <ul class="ticks"><li>Proin a nulla ut purus efficitur vestibulum.</li><li>Nam bibendum ex ut aliquet vulputate.</li><li>Donec id dolor non nisi pellentesque lacinia.</li><li>Fusce efficitur velit ac enim tempus, non pulvinar tortor fermentum.</li></ul>
    <span class="btn" style="left:40px;top:247px">Weiterlesen →</span>
  </div>
  <div class="abs" style="left:600px;top:982px;width:425px;height:337px;background:linear-gradient(135deg,#bfc4c9,#e6e7e9 50%,#2d3440)" role="img" aria-label="Beratungsgespräch zwischen zwei Personen am Besprechungstisch"></div>

  <!-- pricing -->
  <div class="sec-head" style="top:1406px"><div class="mark"></div><div class="kicker">ANGEBOT</div><h2>WÄHLEN SIE DEN BESTEN PREIS</h2></div>

  <div class="price" style="left:211px"><h4>DAS MINIMAL<br>FUNKTIONSFÄHIGES PORTFOLIO</h4><div class="amt">ab 50€</div><p>Sed ut perspiciatis unde omnis iste natus error sit voluptatem rem aperiam accusantium dolorem-que laudantium.</p><ul class="ticks"><li>Suspendisse mattis dui nec commodo aliquam.</li><li>Proin a nulla ut purus efficitur vestibulum.</li><li>Nam bibendum ex ut aliquet vulputate.</li><li>Donec id dolor non nisi pellentesque lacinia.</li></ul><span class="btn" style="left:76px;top:284px">Weiterlesen →</span></div>
  <div class="price featured" style="left:473px"><h4>FINANZPLAN &amp;<br>VERMÖGENSMANAGEMENT</h4><div class="amt">ab 600€</div><p>Sed ut perspiciatis unde omnis iste natus error sit voluptatem rem aperiam accusantium dolorem-que laudantium.</p><ul class="ticks"><li>Suspendisse mattis dui nec commodo aliquam.</li><li>Proin a nulla ut purus efficitur vestibulum.</li><li>Nam bibendum ex ut aliquet vulputate.</li><li>Donec id dolor non nisi pellentesque lacinia.</li></ul><span class="btn ghost" style="left:76px;top:284px">Weiterlesen →</span></div>
  <div class="price" style="left:734px"><h4>INDIVIDUELLES COACHING<br>&amp; BERATUNG</h4><div class="amt">ab 400€</div><p>Sed ut perspiciatis unde omnis iste natus error sit voluptatem rem aperiam accusantium dolorem-que laudantium.</p><ul class="ticks"><li>Suspendisse mattis dui nec commodo aliquam.</li><li>Proin a nulla ut purus efficitur vestibulum.</li><li>Nam bibendum ex ut aliquet vulputate.</li><li>Donec id dolor non nisi pellentesque lacinia.</li></ul><span class="btn" style="left:76px;top:284px">Weiterlesen →</span></div>

  <!-- about -->
  <section class="about">
    <div class="about-photo">
      <svg width="551" height="568" viewBox="0 0 551 568"><path d="M0 0 H370 C470 70 555 180 551 300 C545 430 470 520 390 568 H0Z" fill="#5f86b5"/><path d="M0 0 H352 C452 70 535 180 531 300 C525 430 452 520 372 568 H0Z" fill="#9aa6b3"/></svg>
      <div class="abs" style="left:0;top:0;width:530px;height:568px;clip-path:path('M0 0 H352 C452 70 535 180 531 300 C525 430 452 520 372 568 H0Z');background:linear-gradient(160deg,#c8cdd3,#8e98a4 50%,#1f2d45)" role="img" aria-label="Porträt des Finanzberaters im dunklen Sakko mit verschränkten Armen"></div>
    </div>
    <div class="about-text">
      <div class="kicker">WARUM UNS WÄHLEN</div>
      <h2>SEIT ÜBER 20 JAHREN IM<br>BEREICH FINANZEN</h2>
      <p>Lorem ipsum dolor sit amet, consectetur adipiscing elit, sed do eiusmod tempor incididunt ut labore et dolore magna aliqua. Ut enim ad minim veniam, quis nostrud exercitation ullamco laboris nisi ut aliquip ex ea commodo consequat.</p>
      <div class="feature"><svg class="ic" viewBox="0 0 36 36" fill="none" stroke="#cfe0f5" stroke-width="1.6"><circle cx="18" cy="18" r="13"/><circle cx="18" cy="18" r="6"/><path d="M18 18 L30 6"/></svg><div><h5>Finanzmanagement und Beratung</h5><p>Diam vel quam elementum pulvinar ac tium aenean<br>pharetra magna ac placerat quis eget.</p></div></div>
      <div class="feature"><svg class="ic" viewBox="0 0 36 36" fill="none" stroke="#cfe0f5" stroke-width="1.6"><rect x="4" y="6" width="26" height="18"/><circle cx="16" cy="18" r="5"/><path d="M20 22 L26 30"/></svg><div><h5>Marktforschung und -analyse</h5><p>Diam vel quam elementum pulvinar ac tium aenean<br>pharetra magna ac placerat quis eget.</p></div></div>
      <div class="feature"><svg class="ic" viewBox="0 0 36 36" fill="none" stroke="#cfe0f5" stroke-width="1.6"><circle cx="12" cy="12" r="5"/><circle cx="25" cy="14" r="5"/><path d="M3 32 C3 22 21 22 21 32 M17 32 C17 24 34 24 34 32"/></svg><div><h5>Technologieberatung</h5><p>Diam vel quam elementum pulvinar ac tium aenean<br>pharetra magna ac placerat quis eget.</p></div></div>
    </div>
    <span class="btn ghost" style="left:625px;top:462px">ERSTGESPRÄCH BUCHEN →</span>
  </section>

  <!-- news -->
  <div class="sec-head" style="top:2681px"><div class="mark"></div><div class="kicker" style="font-size:16px">BLEIBEN SIE MIT JONAS VERHELST AUF DEM LAUFENDEN</div><h2>VON DEN NEUESTEN &amp; BELIEBTEN NEWS</h2></div>

  <article class="news" style="left:242px"><div class="img" style="background:linear-gradient(135deg,#2d3138,#8b9097)" role="img" aria-label="Nahaufnahme einer Industriemaschine"><span class="date">July 19<br>2021</span></div><div class="body"><div class="cat">🗀 Artificial Store</div><h4>Repeated of endeavor mr position kindness.</h4><p>Lorem ipsum dolor sit amet, consectetur adipiscing elit, sed do eiusmod tempor incid-idunt ut labore.</p></div><span class="arrow">→</span></article>
  <article class="news" style="left:487px"><div class="img" style="background:linear-gradient(135deg,#6f8aa8,#c7b9a0)" role="img" aria-label="Mitarbeiter in einer Fertigungshalle"><span class="date">July 19<br>2021</span></div><div class="body"><div class="cat">🗀 Automation</div><h4>Justifying Automation in Your Factory.</h4><p>Lorem ipsum dolor sit amet, consectetur adipiscing elit, sed do eiusmod tempor incid-idunt ut labore.</p></div><span class="arrow">→</span></article>
  <article class="news" style="left:731px"><div class="img" style="background:linear-gradient(135deg,#9ea3a9,#4b5058)" role="img" aria-label="Roboterarm in einer Produktionsanlage"><span class="date">July 19<br>2021</span></div><div class="body"><div class="cat">🗀 Digitalization</div><h4>Boost Your Cobot Safety Know-How with These Digital Resources</h4><p>Lorem ipsum dolor sit amet, consectetur adipiscing elit, sed do eiusmod tempor incid-idunt ut labore.</p></div><span class="arrow">→</span></article>

  <!-- contact -->
  <div class="contact-bg"></div>
  <div class="c-shadow"></div>
  <div class="c-box">
    <div class="c-item"><svg width="24" height="24" viewBox="0 0 24 24" fill="#fff"><path d="M12 2a6 6 0 0 0-6 6c0 5 6 12 6 12s6-7 6-12a6 6 0 0 0-6-6zm0 8.5A2.5 2.5 0 1 1 12 5.5a2.5 2.5 0 0 1 0 5z"/></svg><div><h5>KAPITALRUHE</h5><p>Lindenbogen 7<br>20999 Hafenstadt</p></div></div>
    <div class="c-item"><svg width="24" height="24" viewBox="0 0 24 24" fill="#fff"><path d="M6.6 10.8a15 15 0 0 0 6.6 6.6l2.2-2.2c.3-.3.7-.4 1-.2 1.1.4 2.3.6 3.6.6.6 0 1 .4 1 1V20c0 .6-.4 1-1 1A17 17 0 0 1 3 4c0-.6.4-1 1-1h3.5c.6 0 1 .4 1 1 0 1.3.2 2.5.6 3.6.1.3 0 .7-.2 1z"/></svg><div><h5>Einen Anruf tätigen</h5><p>012 / 34567890</p></div></div>
    <div class="c-item"><svg width="24" height="24" viewBox="0 0 24 24" fill="#fff"><path d="M2 9l10-6 10 6v11H2z" opacity=".6"/><path d="M2 9l10 7 10-7v11H2z"/></svg><div><h5>Senden Sie eine E-Mail</h5><p>info@kapitalruhe.example</p></div></div>
  </div>
  <div class="form">
    <div class="kicker">WIR FREUEN UNS JEDERZEIT VON IHNEN ZU HÖREN</div>
    <h3>MACHEN SIE SICH BEREIT, IHR PROJEKT MIT UNS ZU STARTEN</h3>
  </div>
  <div class="field" style="left:537px;top:3371px;width:413px">Name</div>
  <div class="field" style="left:537px;top:3414px;width:187px">Email*</div>
  <div class="field" style="left:762px;top:3414px;width:188px">Telefon</div>
  <div class="field" style="left:537px;top:3458px;width:413px;height:100px">Erzählen Sie uns über das Projekt*</div>
  <span class="btn btn-dark" style="left:537px;top:3600px">Nachricht Senden ➤</span>

  <!-- footer -->
  <svg class="abs" style="left:0;top:3690px" width="1200" height="309" viewBox="0 0 1200 309"><path d="M0 20 C200 -10 420 40 620 30 C850 18 1000 0 1200 15 L1200 309 L0 309Z" fill="#3f6b9c"/></svg>
  <nav class="foot-links"><span>STARTSEITE</span><span>MEIN ANGEBOT</span><span>ÜBER MICH</span><span style="margin-left:28px">ÜBER UNS</span><span>BLOG</span><span>KONTAKT</span></nav>
  <div class="copy">COPYRIGHT © 2021. ALL RIGHTS RESERVED.</div>
  <div class="logo" style="left:509px;top:3910px;color:var(--white)"><i class="dot"></i><span>KAPITALRUHE</span></div>
</div>
</body>
</html>
```